依頼詳細
認知度が低いので、チラシを配ることにより集客につなげたい。

記載項目
社名/電話番号/URL/料金表/特徴/ほか
サイズ
A4
ページ数
両面
希望イメージ
シンプル 複雑
単色 カラフル
暗い 明るい
日常 高級
遊び心 厳粛
未来的 伝統的
女性的 男性的
希望する色
紫系
納品ファイル
• 高解像度JPG (.jpg)
• イラストレーター形式 (.ai)
• PNG形式 (.png)
補足説明
現状のパンフレットではわかりにくい部分もありますので、変更したいと思っています。
QRコードの画像を追加しました。

社名(スクール名)にインパクトを持たせた点が高評価。
メリハリの付いた構成で好感を持てます。
弊社が伝えたいこともよく伝わった感が有りますので採択しました。

素晴らしいものが多く非常に迷いました。
皆さんありがとうございました。

```html
<!DOCTYPE html>
<html lang="ja">
<head>
<meta charset="UTF-8">
<title>あおぞらドローンスクール</title>
<link href="https://fonts.googleapis.com/css2?family=Noto+Sans+JP:wght@400;700;900&display=swap" rel="stylesheet">
<style>
  :root {
    --sky-top: #2f5d7e;
    --sky-mid: #8fb6cf;
    --field: #5f8f3a;
    --field-light: #a9c46a;
    --orange: #f08a00;
    --orange-deep: #e06c00;
    --red: #e2001a;
    --ink: #2b2b2b;
    --label: #8a2a12;
    --paper: #ffffff;
  }
  * { margin: 0; padding: 0; box-sizing: border-box; }
  html, body { width: 849px; height: 1200px; overflow: hidden; background: var(--paper); }
  body { font-family: "Noto Sans JP", sans-serif; color: var(--ink); }
  .flyer { position: relative; width: 849px; height: 1200px; overflow: hidden; background: var(--paper); }

  .hero-photo {
    position: absolute; left: 0; top: 0; width: 849px; height: 620px;
    background: linear-gradient(180deg, var(--sky-top) 0%, #4f7fa0 18%, var(--sky-mid) 40%, #cfdfe6 52%, var(--field-light) 64%, var(--field) 100%);
  }
  .headline {
    position: absolute; top: 24px; left: 0; width: 100%; text-align: center;
    font-weight: 900; font-size: 56px; line-height: 1.3; color: #fff; letter-spacing: 1px;
    text-shadow: 0 2px 6px rgba(0,0,0,.35);
  }
  .white-arch { position: absolute; left: 0; top: 380px; width: 849px; height: 820px; }

  .accreditation {
    position: absolute; top: 262px; left: 0; width: 100%; text-align: center;
    font-weight: 900; font-size: 32px; line-height: 1.35; color: var(--ink);
  }

  .school-name {
    position: absolute; top: 0; left: 0; width: 100%; height: 0;
    font-weight: 900; color: var(--orange); line-height: 1;
  }
  .school-name span { position: absolute; left: 0; width: 100%; text-align: center; }
  .school-name .line1 { top: 392px; font-size: 108px; letter-spacing: 4px; }
  .school-name .line2 { top: 508px; font-size: 108px; letter-spacing: 4px; }
  .school-name .line3 { top: 624px; font-size: 46px; letter-spacing: 2px; }

  .trial-badge {
    position: absolute; left: 690px; top: 470px; width: 144px; height: 112px;
    border: 3px solid var(--orange); border-radius: 8px; background: #fff;
    text-align: center; padding-top: 12px;
  }
  .trial-badge .small { display: block; font-size: 16px; font-weight: 700; color: var(--orange-deep); line-height: 1.3; }
  .trial-badge .big { display: block; font-size: 28px; font-weight: 900; color: var(--red); margin-top: 4px; line-height: 1.3; }

  .side-catch {
    position: absolute; left: 30px; top: 660px; height: 300px;
    writing-mode: vertical-rl; font-weight: 900; font-size: 21px; line-height: 1.2; color: var(--ink);
    letter-spacing: 1px;
  }

  .intro {
    position: absolute; left: 175px; top: 690px; width: 648px;
    font-size: 14px; line-height: 1.8; text-align: justify;
  }

  .fields {
    position: absolute; left: 170px; top: 840px; width: 655px;
    display: flex; justify-content: space-between;
  }
  .field-item { width: 150px; text-align: center; }
  .field-photo {
    width: 124px; height: 124px; margin: 0 auto; border-radius: 50%;
    background: radial-gradient(circle at 50% 35%, #cfe0ea 0%, #8fae7a 60%, #5c7f3f 100%);
  }
  .field-photo.square { border-radius: 6px; background: linear-gradient(180deg, #c8d8d0 0%, #6e9a4a 100%); }
  .field-label { margin-top: 8px; font-size: 28px; font-weight: 900; line-height: 1.3; color: var(--label); }

  .certificate {
    position: absolute; top: 1030px; left: 0; width: 100%; text-align: center; line-height: 1.3;
  }
  .certificate span {
    font-size: 50px; font-weight: 900; color: var(--red);
    border-bottom: 3px solid var(--red); padding-bottom: 2px;
  }
  .note {
    position: absolute; top: 1120px; left: 0; width: 100%; text-align: center;
    font-size: 18px; line-height: 1.6;
  }
</style>
</head>
<body>
<div class="flyer">
  <div class="hero-photo" role="img" aria-label="青空を飛ぶドローンと広がる田園風景の写真"></div>
  <h1 class="headline">ドローンを学びたい方、必見!</h1>

  <svg class="white-arch" viewBox="0 0 849 820" aria-hidden="true">
    <path d="M0 220 Q424 -80 849 220 L849 820 L0 820 Z" fill="#ffffff"/>
  </svg>

  <p class="accreditation">国土交通省<br>ドローン管理団体認定校</p>

  <h2 class="school-name">
    <span class="line1">あおぞら</span>
    <span class="line2">ドローン</span>
    <span class="line3">スクール</span>
  </h2>

  <div class="trial-badge">
    <span class="small">初めての方<br>大歓迎!</span>
    <span class="big">無料体験</span>
  </div>

  <p class="side-catch">様々な分野で活躍できます!</p>

  <p class="intro">私たちは、福岡県でドローンの初心者から、産業用ドローンのプロフェッショナルまで、必要に応じたカリキュラムで、親切丁寧にそして実践的な教育を行っています。初心者の方には基本的な構造や用語、操縦に関する法令から、上級者の方には特殊機能や撮影方法、農薬散布の方法なども的確にご指導いたします。また、農業散布専用コースもございますので、農業に従事している方は是非ご活用ください。</p>

  <div class="fields">
    <div class="field-item">
      <div class="field-photo square" role="img" aria-label="畑で農薬を散布するドローンの写真"></div>
      <p class="field-label">農薬散布</p>
    </div>
    <div class="field-item">
      <div class="field-photo" role="img" aria-label="空撮を行うドローンの写真"></div>
      <p class="field-label">空撮</p>
    </div>
    <div class="field-item">
      <div class="field-photo" role="img" aria-label="測量作業に使われるドローンの写真"></div>
      <p class="field-label">測量</p>
    </div>
    <div class="field-item">
      <div class="field-photo" role="img" aria-label="橋梁を点検するドローンの写真"></div>
      <p class="field-label">点検</p>
    </div>
  </div>

  <p class="certificate"><span>技能検定合格証を取得可能!</span></p>
  <p class="note">国土交通省認定校ですから、各コース受講後に検定試験を行います。<br>検定に合格すると技能検定合格証を発行いたします。</p>
</div>
</body>
</html>
```